We need letterhead, Business Cards, and envelops designed. We have attached a design of our logo and a sample of letterhead idea that was started but never perfected, it is only an idea for the letterhead if you can design something better we may love that also we are open to change.
We want a design that looks professional in style. we are a non profit trade association in the construction industry. the green color in the attached design represent green building, and we like that. also if you just want to enhance the letterhead sample that we attached that would be fine also.
Thanks and good luck
also the name that should show on the first business cards should be Merwin Haskell, Director are web address is www.vtqpa.org

```html
<!DOCTYPE html>
<html lang="en">
<head>
<meta charset="utf-8">
<title>VTQPA Letterhead</title>
<link href="https://fonts.googleapis.com/css2?family=Questrial&display=swap" rel="stylesheet">
<style>
  :root {
    --ink: #000000;
    --paper: #ffffff;
    --leaf: #3f7a1b;
    --leaf-light: #94d95f;
    --panel-text: #ffffff;
  }
  html, body {
    margin: 0;
    padding: 0;
    width: 1200px;
    height: 600px;
    overflow: hidden;
    background: var(--paper);
  }
  .letterhead {
    position: relative;
    width: 1200px;
    height: 600px;
    background: var(--paper);
    font-family: "Questrial", "Century Gothic", sans-serif;
  }
  .side-panel {
    position: absolute;
    left: 0;
    top: 0;
    width: 322px;
    height: 600px;
    background: var(--ink);
    color: var(--panel-text);
  }
  .address {
    position: absolute;
    left: 48px;
    top: 68px;
    margin: 0;
    font-size: 17px;
    line-height: 23px;
    letter-spacing: 2.2px;
    font-style: normal;
  }
  .contact-list {
    position: absolute;
    left: 48px;
    top: 180px;
    margin: 0;
    padding: 0;
    list-style: none;
    font-size: 17px;
    line-height: 23px;
    letter-spacing: 2.2px;
  }
  .contact-item {
    display: flex;
    align-items: center;
  }
  .contact-icon {
    width: 13px;
    height: 13px;
    margin-right: 31px;
    flex: none;
  }
  .contact-icon * {
    fill: none;
    stroke: var(--leaf);
    stroke-width: 1.6;
  }
  .skyline-art {
    position: absolute;
    left: 46px;
    top: 387px;
    width: 237px;
    height: 213px;
    background: linear-gradient(180deg, var(--leaf) 0%, #4f8f26 60%, var(--leaf) 100%);
  }
  .association-mark {
    position: absolute;
    left: 366px;
    top: 58px;
    display: flex;
    align-items: center;
    gap: 14px;
  }
  .mark-square {
    width: 22px;
    height: 22px;
    background: var(--leaf);
  }
  .association-name {
    font-size: 64px;
    line-height: 1;
    letter-spacing: 6px;
    color: var(--ink);
  }
</style>
</head>
<body>
  <main class="letterhead">
    <aside class="side-panel">
      <address class="address">
        address<br>
        1875 oakridge road<br>
        millbrook, ST 95014
      </address>
      <ul class="contact-list">
        <li class="contact-item">
          <svg class="contact-icon" viewBox="0 0 14 14" aria-label="Phone">
            <path d="M2 5 Q7 1 12 5 L10.5 6.5 L9 5.5 L5 5.5 L3.5 6.5 Z"/>
            <rect x="3" y="7.5" width="8" height="5" rx="1"/>
          </svg>
          <span>555-210-4476</span>
        </li>
        <li class="contact-item">
          <svg class="contact-icon" viewBox="0 0 14 14" aria-label="Fax">
            <rect x="4" y="1.5" width="6" height="4"/>
            <rect x="1.5" y="5.5" width="11" height="5"/>
            <rect x="4" y="9" width="6" height="3.5"/>
          </svg>
          <span>555-210-4477</span>
        </li>
        <li class="contact-item">
          <svg class="contact-icon" viewBox="0 0 14 14" aria-label="Website">
            <circle cx="7" cy="7" r="5.5"/>
            <path d="M1.5 7 H12.5 M7 1.5 Q3.5 7 7 12.5 M7 1.5 Q10.5 7 7 12.5"/>
          </svg>
          <span>www.vtqpa.org</span>
        </li>
      </ul>
      <div class="skyline-art" role="img" aria-label="Decorative green building skyline artwork"></div>
    </aside>

    <header class="association-mark">
      <span class="mark-square"></span>
      <span class="association-name">VTQPA</span>
    </header>
  </main>
</body>
</html>
```